Specialist Medical Group Brochure for General Practitioners (GPs)

We need a brochure to give to General Practitioners. We are a group of medical specialists offering fast appointments for GPs and their patients. The service is called Tandem Consult Medicine. Our old brochure has been uploaded and we wish to update it with our new logo and colour scheme. For specialist photos - we need 16 frames,
Please also refer to our website to understand our theme :
www.prlv.com.au.
And more information on the service :
https://prlv.com.au/specialist-support
The final design should be modern and communicate positive, friendly, fast and easy support. No whitecoats, wheelchairs, or hospital beds please.
Updates
Need extra days to review
Target Market(s)
General Practitioners
Colors
Designer to choose colors to be used in the design.
Requirements
Must have
- Photos of specialists - 16 of them
Colours from logo and website
Pastel colours
Nice to have
- SImilar theme to website photos and photos of old brochure.
Modern
Should not have
- White Coat, Wheelchairs, Hospitals, Hospital Beds, Nurses

```html
<!DOCTYPE html>
<html lang="en">
<head>
<meta charset="utf-8">
<title>Tandem Consult Medicine – Brochure Cover</title>
<link rel="stylesheet" href="https://fonts.googleapis.com/css2?family=Montserrat:wght@400;800&display=swap">
<style>
  :root {
    --canvas: #cfd1cf;
    --paper: #f2f1f1;
    --mist-top: #f5f4f4;
    --mist-mid: #ebe9e9;
    --mist-horizon: #dedbdb;
    --mist-ground: #d6d3d3;
    --brand-teal: #8dbdae;
    --brand-grey: #8a8281;
    --sand: #cdc6c1;
    --ink: #2a2625;
  }
  * { margin: 0; padding: 0; box-sizing: border-box; }
  html, body {
    width: 1200px;
    height: 800px;
    overflow: hidden;
    background: var(--canvas);
  }
  .brochure-cover {
    position: absolute;
    left: 430px;
    top: 40px;
    width: 340px;
    height: 720px;
    background: var(--paper);
    overflow: hidden;
    box-shadow: 0 10px 24px rgba(0, 0, 0, 0.18);
  }
  .cover-photo {
    position: absolute;
    inset: 0;
    background:
      linear-gradient(180deg,
        transparent 0%,
        transparent 40%,
        rgba(190, 186, 186, 0.35) 44%,
        rgba(190, 186, 186, 0.1) 47%,
        transparent 52%,
        transparent 100%),
      linear-gradient(180deg,
        var(--mist-top) 0%,
        var(--mist-mid) 38%,
        var(--mist-horizon) 46%,
        #e4e2e2 60%,
        var(--mist-ground) 100%);
  }
  .brand {
    position: absolute;
    top: 38px;
    left: 30px;
    display: flex;
    align-items: center;
    gap: 10px;
    font-family: "Montserrat", sans-serif;
    font-weight: 400;
    color: var(--brand-grey);
  }
  .brand-dot {
    width: 54px;
    height: 54px;
    border-radius: 50%;
    background: var(--brand-teal);
    flex: none;
  }
  .brand-name {
    display: flex;
    flex-direction: column;
    line-height: 1;
  }
  .brand-name .main {
    font-size: 26px;
    letter-spacing: 0.5px;
  }
  .brand-name .sub {
    font-size: 9px;
    letter-spacing: 0.6px;
    margin-top: 4px;
  }
  .title-band {
    position: absolute;
    inset: 0;
    width: 340px;
    height: 720px;
  }
  .cover-title {
    position: absolute;
    left: 112px;
    top: 536px;
    font-family: "Montserrat", sans-serif;
    font-weight: 800;
    font-size: 32px;
    line-height: 1.12;
    color: var(--ink);
  }
</style>
</head>
<body>
  <section class="brochure-cover">
    <div class="cover-photo" role="img" aria-label="Photograph of a lone person walking across a vast pale misty plain under a white sky"></div>

    <div class="brand">
      <span class="brand-dot"></span>
      <span class="brand-name">
        <span class="main">PARALLEL VALE</span>
        <span class="sub">OCCUPATIONAL MEDICINE</span>
      </span>
    </div>

    <svg class="title-band" viewBox="0 0 340 720" aria-hidden="true">
      <circle cx="370" cy="735" r="315" fill="var(--sand)"/>
    </svg>

    <h1 class="cover-title">Tandem<br>Consult<br>Medicine</h1>
  </section>
</body>
</html>
```